IT company website design

Require a home page and an inner page designed for a company located in Ohio. The company deals with a wide range of IT services like Software development, IT based education services such as digital textbooks and BPO

Would like to get a Home page for the website and an inner page to be designed.

Design must be modern, clean and very professional. The home page should have a carousel of our services for which content will be provided.

It should give a feel that we are a large company to our prospective customers.
Updates

Hi,
In the few designs I have got for the home page, there are mockups with unwanted content/blocks like ex. latest blog posts or similar blocks. Kindly note that, we don't want this. Please follow the information about content on the home page as mentioned in the project brief. Designers, who have already submitted designs, if you can remove the unwanted blocks, it will be really appreciated.

Thanks.

I have received over 9 designs for this project, but none of them seem to be custom designed for my needs. They are just re-use of previous designs and look very out dated. Looking for fresh, clean designs following latest design trends like the ones you see in pixelbazaar etc.

If you can provide me a design that meets my expectations, I can definitely UP my budget for you .

Industry/Entity Type

Education

Requirements
Must have
• > > Home page > >
Home page will have

* Top Menu: Home, About Us, Solutions, Services, Contact us (should have space to accommodate for more)

* Should have a flash carousel/slide show. Each slide should be about a service we provide. Ex. a slide for bpo will have the content "Bridging the quality and cost divide in outsourcing" It should be depicted by an illustration or photograph. If you are going to use photograph, please use ones for framelode.com

* Textual content of about 200 words which we will provide

* Links in the footer along with a copyright, legal notice etc.

* Importantly, the home page should have 2 fancy buttons for "Member Login" and "Online Tutoring"

> > Inner pages > >
Will be mainly textual content explaining each of the service so, should have space for lots of textual content, with a fancy, page title (usually the service name). All inner pages should also have a side menu or something like that from where users can have a one click access to all our services.

Our logo is blue in color. with color code "0080FB". It just a stylized D with rest of the text i.e Quorvane Tech Inc. our logo is of the proportion. 1:5 i.e 60px height, 300px wide. We can proportionately increase or decrease the dimensions as necessary. Color combination of the sight should be something that will go with this.

```html
<!DOCTYPE html>
<html lang="en">
<head>
<meta charset="utf-8">
<title>Quorvane Tech Inc.</title>
<link rel="stylesheet" href="https://fonts.googleapis.com/css2?family=Carlito:wght@400;700&family=Lato:wght@400&family=PT+Serif:wght@700&family=PT+Sans:wght@400&display=swap">
<style>
:root{
  --brand:#0a7ff8;
  --brand-dark:#0668d8;
  --ribbon:#aad5fb;
  --nav-link:#1f5fae;
  --body-text:#2b5e9c;
  --heading:#141414;
  --bar-dark:#1c1c1c;
  --bar-mid:#2a2a2a;
  --sky:#d7eafc;
  --ring:#e6e6e6;
  --footer-link:#2184c8;
  --footer-copy:#d8d8d8;
}
*{margin:0;padding:0;box-sizing:border-box}
html,body{width:1200px;height:1066px;overflow:hidden}
body{position:relative;background:#fff;font-family:"Carlito",sans-serif}
.top-bar{position:absolute;left:0;top:0;width:1200px;height:66px;
  background:linear-gradient(90deg,var(--bar-dark),var(--bar-mid) 30%,#222 55%,var(--bar-mid) 80%,var(--bar-dark))}
.main-nav{position:absolute;left:153px;top:13px;display:flex;align-items:center;height:42px}
.main-nav a{font-family:Arial,Helvetica,sans-serif;font-size:17px;color:var(--nav-link);text-decoration:none;margin-right:47px}
.main-nav a.active{background:var(--brand);color:#fff;width:90px;height:42px;display:flex;align-items:center;justify-content:center;
  outline:1px dashed rgba(255,255,255,.7);outline-offset:-4px;border:1px solid #4aa2ff;margin-right:27px}
.sky-band{position:absolute;left:0;top:481px;width:1200px;height:482px;background:linear-gradient(var(--sky),#fff)}
.brand-name{position:absolute;left:153px;top:100px;display:flex;align-items:center;gap:10px;
  font-family:"Carlito",sans-serif;font-size:30px;color:var(--brand)}
.brand-name .dot{width:24px;height:24px;border-radius:50%;background:var(--brand)}
.cta{position:absolute;top:92px;width:163px;height:40px;border-radius:20px;
  background:linear-gradient(#5cb3ff,var(--brand) 55%,var(--brand-dark));border:1px solid #0b63c8;
  box-shadow:inset 0 1px 0 rgba(255,255,255,.6);color:#fff;font-family:"PT Sans",sans-serif;font-size:14.5px;
  display:flex;align-items:center;justify-content:center;text-decoration:none;letter-spacing:.2px}
.cta.login{left:728px}
.cta.tutorial{left:899px}
.slider{position:absolute;left:151px;top:165px;width:911px;height:403px;background:var(--brand)}
.slide-art{position:absolute;left:0;top:0}
.slide-title{position:absolute;left:194px;top:280px;font-family:"PT Serif",serif;font-weight:700;line-height:1;text-transform:none}
.slide-title span{display:block}
.slide-title .l1{font-size:56px;color:var(--brand);letter-spacing:.5px}
.slide-title .l2{font-size:46px;color:var(--heading);margin-top:-9px}
.slide-title .l3{font-size:37px;color:var(--heading);margin-top:2px}
.slide-title .l4{font-size:33px;color:var(--brand);margin-top:4px}
.slide-title small{font-size:26px}
.intro{position:absolute;left:147px;top:624px;width:911px}
.intro h1{font-family:"Lato",sans-serif;font-weight:400;font-size:26.5px;line-height:30px;color:var(--heading);margin-left:3px;margin-bottom:20px}
.intro p{font-size:15.2px;line-height:18px;color:var(--body-text);text-align:justify;margin-bottom:18px}
.footer{position:absolute;left:0;top:963px;width:1200px;height:103px;border-top:7px solid #000;
  background:linear-gradient(90deg,var(--bar-dark),var(--bar-mid) 35%,#232323 60%,var(--bar-mid) 85%,var(--bar-dark))}
.footer-nav{position:absolute;left:134px;top:33px;font-size:15.5px;color:var(--footer-link)}
.footer-nav a{color:var(--footer-link);text-decoration:none}
.footer-nav .sep{margin:0 10px}
.copyright{position:absolute;left:134px;top:59px;font-size:13px;color:var(--footer-copy)}
.copyright a{color:var(--footer-link);margin-left:6px}
.copyright .sep{margin:0 4px 0 6px;color:var(--footer-link)}
</style>
</head>
<body>
<header class="top-bar">
  <nav class="main-nav">
    <a class="active" href="#">Home</a>
    <a href="#">About Us</a>
    <a href="#">Solutions</a>
    <a href="#">Services</a>
    <a href="#">Contact us</a>
  </nav>
</header>

<div class="sky-band"></div>

<div class="brand-name"><span class="dot"></span>Quorvane Tech Inc.</div>
<a class="cta login" href="#">MEMBER LOGIN</a>
<a class="cta tutorial" href="#">ONLINE TUTORIAL</a>

<section class="slider"></section>
<svg class="slide-art" width="1200" height="600" viewBox="0 0 1200 600">
  <defs>
    <radialGradient id="photoTone" cx="45%" cy="40%" r="65%">
      <stop offset="0" stop-color="#e9ddd4"/>
      <stop offset=".55" stop-color="#b8c4cf"/>
      <stop offset="1" stop-color="#6f8194"/>
    </radialGradient>
    <filter id="ribbonShadow" x="-10%" y="-10%" width="120%" height="140%">
      <feDropShadow dx="0" dy="6" stdDeviation="5" flood-color="#003a80" flood-opacity=".45"/>
    </filter>
  </defs>
  <polygon points="142,447 151,447 151,455" fill="#0a3566"/>
  <polygon points="142,276 573,276 533,361 573,447 142,447" fill="var(--ribbon)" filter="url(#ribbonShadow)"/>
  <circle cx="818" cy="352" r="203" fill="var(--ring)"/>
  <circle cx="818" cy="352" r="195" fill="url(#photoTone)" role="img" aria-label="Photo of smiling call-centre agents wearing headsets"/>
  <circle cx="199" cy="531" r="7" fill="#fff"/>
  <circle cx="215" cy="531" r="4" fill="#fff"/>
  <circle cx="231" cy="531" r="4" fill="#fff"/>
  <circle cx="247" cy="531" r="4" fill="#fff"/>
  <circle cx="263" cy="531" r="4" fill="#fff"/>
  <g aria-label="Previous slide">
    <circle cx="124" cy="356" r="14" fill="#e4e4e4" stroke="#fff" stroke-width="2"/>
    <path d="M127 349 L120 356 L127 363" fill="none" stroke="#444" stroke-width="2.6"/>
  </g>
  <g aria-label="Next slide">
    <circle cx="1086" cy="360" r="14" fill="#e4e4e4" stroke="#fff" stroke-width="2"/>
    <path d="M1083 353 L1090 360 L1083 367" fill="none" stroke="#444" stroke-width="2.6"/>
  </g>
</svg>
<h2 class="slide-title">
  <span class="l1">BRIDGING</span>
  <span class="l2">the QUALITY</span>
  <span class="l3">&amp; COST DIVIDE</span>
  <span class="l4"><small>in</small> OUTSOURCING</span>
</h2>

<main class="intro">
  <h1>Suspendisse at magna leo. Morbi feugiat ultrices nisi eget suscipit. Vivamus iaculis quam nec orci iaculis</h1>
  <p>Phasellus ornare imperdiet ornare. Duis vel placerat magna. Cras elit odio, hendrerit quis mattis eu, accumsan vitae metus. Nulla aliquam urna in mauris scelerisque ac imperdiet elit gravida. Pellentesque augue velit, ultrices non laoreet ac, lobortis tincidunt quam. Sed orci orci, interdum euismod cursus et, porttitor in arcu. Maecenas a facilisis augue.</p>
  <p>Duis non commodo sem. Donec sagittis enim vulputate sem adipiscing fringilla. Praesent rhoncus euismod posuere. Proin sagittis varius mi, ut laoreet sem lacinia vestibulum. Donec nec ante non lorem sollicitudin tincidunt. raesent rhoncus euismod posuere. Proin sagittis varius mi, ut laoreet sem lacinia vestibulum.</p>
  <p>Suspendisse ac urna sapien. Donec ornare facilisis egestas. Morbi vel felis at est aliquet ornare nec id massa. In faucibus ornare enim eget porta. Proin et dui purus, sit amet iaculis metus. Curabitur vestibulum, nisi vitae vestibulum imperdiet, quam augue pretium ipsum, quis varius nisi est sed felis. Cras nunc massa, tincidunt quis rutrum eget, lobortis consectetur enim. Sed fringilla placerat nunc id mattis.</p>
</main>

<footer class="footer">
  <nav class="footer-nav">
    <a href="#">Home</a><span class="sep">|</span>
    <a href="#">About Us</a><span class="sep">|</span>
    <a href="#">Solutions</a><span class="sep">|</span>
    <a href="#">Services</a><span class="sep">|</span>
    <a href="#">Contact us</a>
  </nav>
  <p class="copyright">copyright 2011 Quorvane Tech Inc. <a href="#">Privacy Policy</a><span class="sep">|</span><a href="#" style="margin-left:0">Terms and Policies</a></p>
</footer>
</body>
</html>
```